Halvorsen Partners Business Card

Halvorsen Partners Civil Construction
Marcus Halvorsen
CEO
727-518-6094
Marcus@HalvorsenSiteworks.example
www.HalvorsenSiteworks.example
Site Development
Utility Construction
Excavation
40876 County Lane 19
Land O' Lakes, FL 34638

Target Market(s)

Construction and government

Industry/Entity Type

Business

Contact Information for Business Card

I want an unique design that make a statement

Number of Pages Required

1 page

Font styles to use

Colors

Designer to choose colors to be used in the design.

Requirements
Must have
• unique design, feel free to modify or change the color of my logo.
Nice to have
• extra design features like spot UV, foil accents, color edges, unique paper, or any thing that would make my card pop.
• I like the feel of the image that I attached

```html
<!DOCTYPE html>
<html lang="en">
<head>
<meta charset="utf-8">
<title>Halvorsen Partners Business Card</title>
<link rel="stylesheet" href="https://fonts.googleapis.com/css2?family=Lato:wght@400;700&family=Marcellus&display=swap">
<style>
  :root {
    --navy: #27427f;
    --steel: #6b6c6e;
    --paper: #ffffff;
    --backdrop: #2b2b2d;
    --ink-light: #ffffff;
  }
  * { box-sizing: border-box; margin: 0; padding: 0; }
  html, body {
    width: 1200px; height: 852px; overflow: hidden;
    background: var(--backdrop);
  }
  .canvas { position: relative; width: 1200px; height: 852px; }
  .card {
    position: absolute; width: 560px; height: 320px;
    border-radius: 22px; overflow: hidden;
    box-shadow: 0 18px 40px rgba(0,0,0,.45);
  }
  .card--front { left: 60px; top: 80px; background: var(--navy); }
  .card--back { left: 580px; top: 450px; background: var(--paper); }

  .brand { display: flex; align-items: center; gap: 12px; }
  .brand__mark { width: 34px; height: 34px; flex: none; }
  .brand__name {
    font-family: "Marcellus", serif; line-height: 1.05; letter-spacing: .5px;
  }
  .brand__name span { display: block; }
  .brand__name .line-1 { font-size: 21px; }
  .brand__name .line-2 { font-size: 13px; letter-spacing: 3px; }

  .card--front .brand {
    position: absolute; left: 50%; top: 120px; transform: translateX(-50%);
    color: var(--ink-light);
  }
  .card--front .brand__mark { background: var(--ink-light); }
  .services {
    position: absolute; left: 0; right: 0; bottom: 48px; text-align: center;
    font-family: "Lato", sans-serif; font-size: 14px; color: var(--ink-light);
    letter-spacing: .3px;
  }
  .services .sep { margin: 0 8px; opacity: .85; }

  .back-art { position: absolute; inset: 0; width: 560px; height: 320px; }
  .card--back .brand {
    position: absolute; left: 36px; top: 70px; color: var(--navy);
  }
  .card--back .brand__mark { background: var(--navy); }
  .card--back .brand__name .line-2 { color: var(--steel); }

  .person {
    position: absolute; left: 40px; top: 200px; color: var(--ink-light);
    font-family: "Lato", sans-serif;
  }
  .person__name { font-size: 21px; letter-spacing: .8px; text-transform: uppercase; }
  .person__role { font-size: 14px; margin-top: 1px; }
  .contact { list-style: none; margin-top: 8px; font-size: 13px; }
  .contact li { display: flex; align-items: center; gap: 8px; height: 18px; }
  .contact svg { width: 12px; height: 12px; fill: var(--ink-light); flex: none; }
</style>
</head>
<body>
<main class="canvas">

  <section class="card card--front" aria-label="Card front">
    <div class="brand">
      <span class="brand__mark"></span>
      <p class="brand__name">
        <span class="line-1">HALVORSEN PARTNERS</span>
        <span class="line-2">CIVIL CONSTRUCTION</span>
      </p>
    </div>
    <p class="services">
      Site Development<span class="sep">|</span>Utility Construction<span class="sep">|</span>Excavation
    </p>
  </section>

  <section class="card card--back" aria-label="Card back">
    <svg class="back-art" viewBox="0 0 560 320" aria-hidden="true">
      <polygon points="0,185 300,185 460,100 560,100 560,320 0,320" fill="var(--steel)"/>
      <polygon points="330,0 560,0 560,100 460,100" fill="var(--navy)"/>
      <rect x="395" y="20" width="110" height="110" fill="var(--navy)"/>
    </svg>

    <div class="brand">
      <span class="brand__mark"></span>
      <p class="brand__name">
        <span class="line-1">HALVORSEN PARTNERS</span>
        <span class="line-2">CIVIL CONSTRUCTION</span>
      </p>
    </div>

    <div class="person">
      <p class="person__name">Marcus Halvorsen</p>
      <p class="person__role">CEO</p>
      <ul class="contact">
        <li>
          <svg viewBox="0 0 24 24"><path d="M6.6 10.8a15 15 0 0 0 6.6 6.6l2.2-2.2a1 1 0 0 1 1-.25 11.4 11.4 0 0 0 3.6.57 1 1 0 0 1 1 1V20a1 1 0 0 1-1 1A17 17 0 0 1 3 4a1 1 0 0 1 1-1h3.5a1 1 0 0 1 1 1c0 1.25.2 2.45.57 3.57a1 1 0 0 1-.25 1z"/></svg>
          727-518-6094
        </li>
        <li>
          <svg viewBox="0 0 24 24"><path d="M2 5h20v14H2z M3.5 6.5 12 13l8.5-6.5" stroke="#6b6c6e" stroke-width="1.6"/></svg>
          Marcus@HalvorsenSiteworks.example
        </li>
        <li>
          <svg viewBox="0 0 24 24"><circle cx="12" cy="12" r="10"/><path d="M2 12h20M12 2c3 3 3 17 0 20M12 2c-3 3-3 17 0 20" stroke="#6b6c6e" stroke-width="1.4" fill="none"/></svg>
          www.HalvorsenSiteworks.example
        </li>
      </ul>
    </div>
  </section>

</main>
</body>
</html>
```